Tavenorix - world unique technology for better life - please let them know who am i at first sight

We need a new business card for company which is a provider of unique crystal based technology suitable for all living being. For more information and final design you can use our brochure (our colours are black and blue from brochure).
We use Verdana font

Industry/Entity Type

Business

Contact Information for Business Card

regular dimension

Font styles to use
Other font styles liked:
• Verdana

Requirements
Must have
• Logo
• name
• function/position
• phone
• mobile
• e-mail
• adress
Nice to have
• inovative design (technology directed)

```html
<!DOCTYPE html>
<html lang="en">
<head>
<meta charset="utf-8">
<title>Tavenorix Business Card</title>
<link rel="stylesheet" href="https://fonts.googleapis.com/css2?family=Open+Sans:wght@300;400;600&display=swap">
<style>
  :root {
    --ink: #050607;
    --ink-soft: #111417;
    --paper: #f3f4f4;
    --blue: #35b9e0;
    --blue-deep: #1d8fb5;
    --stage: #d9d6d0;
  }
  * { margin: 0; padding: 0; box-sizing: border-box; }
  html, body { width: 1200px; height: 858px; overflow: hidden; }
  body {
    background: var(--stage);
    font-family: "Open Sans", Verdana, sans-serif;
    display: flex;
    align-items: center;
    justify-content: center;
    gap: 44px;
  }
  .card {
    width: 520px;
    height: 297px;
    position: relative;
    overflow: hidden;
    box-shadow: 0 10px 28px rgba(0,0,0,.28);
  }

  /* Front */
  .card-front { background: var(--paper); }
  .front-band {
    position: absolute; left: 0; top: 0; right: 0; height: 160px;
    background: var(--ink);
    display: flex; align-items: center; padding-left: 54px; gap: 22px;
  }
  .brand-dot {
    width: 62px; height: 62px; border-radius: 50%;
    background: var(--blue);
    flex: none;
  }
  .brand-name {
    color: var(--blue);
    font-weight: 300;
    font-size: 46px;
    letter-spacing: 2px;
    text-transform: uppercase;
  }
  .front-details {
    position: absolute; left: 0; right: 0; top: 160px; bottom: 0;
    display: flex; align-items: center; padding: 0 30px;
    color: var(--blue);
  }
  .person { flex: 1; }
  .person-name { font-size: 19px; font-weight: 600; line-height: 1.2; }
  .person-role { font-size: 13px; margin-bottom: 10px; }
  .person-address { font-size: 11px; line-height: 1.5; }
  .divider {
    width: 1px; height: 74px; background: var(--blue); margin: 0 22px;
  }
  .contacts { list-style: none; font-size: 11px; line-height: 1.85; }
  .contacts li { display: flex; align-items: center; gap: 8px; }
  .contacts svg { width: 11px; height: 11px; flex: none; }

  /* Back */
  .card-back { background: var(--ink); }
  .back-texture {
    position: absolute; inset: 0;
    background: radial-gradient(circle at 62% 52%, #1d262c 0%, #0d1114 45%, var(--ink) 75%);
  }
  .back-brand {
    position: absolute; left: 66px; top: 78px;
    display: flex; align-items: center; gap: 22px;
  }
  .back-web {
    position: absolute; left: 66px; right: 66px; bottom: 58px;
    display: flex; align-items: center; gap: 16px;
    color: var(--blue); font-size: 13px;
  }
  .back-web .rule { flex: 1; height: 1px; background: var(--blue); }
</style>
</head>
<body>

  <section class="card card-front" aria-label="Business card front">
    <div class="front-band">
      <span class="brand-dot"></span>
      <span class="brand-name">Tavenorix</span>
    </div>
    <div class="front-details">
      <div class="person">
        <p class="person-name">Employee Name</p>
        <p class="person-role">Employee Position</p>
        <p class="person-address">28-34 Marlow Lane<br>London EC2A 3QT, United Kingdom</p>
      </div>
      <span class="divider"></span>
      <ul class="contacts">
        <li>
          <svg viewBox="0 0 12 12" aria-hidden="true"><rect x="3" y="0.5" width="6" height="11" rx="1" fill="none" stroke="currentColor"/><circle cx="6" cy="9.5" r=".7" fill="currentColor"/></svg>
          + xxx(x) xx xxx xxx
        </li>
        <li>
          <svg viewBox="0 0 12 12" aria-hidden="true"><path d="M2.5 1 L4.5 1 L5.5 3.5 L4 4.5 Q5 7 7.5 8 L8.5 6.5 L11 7.5 L11 9.5 Q10.5 11 9 11 Q1 10 1 2.5 Q1 1 2.5 1Z" fill="currentColor"/></svg>
          +385(0) 51 420 937
        </li>
        <li>
          <svg viewBox="0 0 12 12" aria-hidden="true"><rect x=".5" y="2" width="11" height="8" fill="none" stroke="currentColor"/><path d="M.5 2 L6 6.5 L11.5 2" fill="none" stroke="currentColor"/></svg>
          info@tavenorix.eu
        </li>
        <li>
          <svg viewBox="0 0 12 12" aria-hidden="true"><circle cx="6" cy="6" r="5.3" fill="none" stroke="currentColor"/><ellipse cx="6" cy="6" rx="2.2" ry="5.3" fill="none" stroke="currentColor"/><path d="M.7 6 H11.3" stroke="currentColor"/></svg>
          www.tavenorix.eu
        </li>
      </ul>
    </div>
  </section>

  <section class="card card-back" aria-label="Business card back">
    <div class="back-texture" role="img" aria-label="Faint large decorative crystal pattern in dark blue-grey tones"></div>
    <div class="back-brand">
      <span class="brand-dot"></span>
      <span class="brand-name">Tavenorix</span>
    </div>
    <div class="back-web">
      <span>www.tavenorix.eu</span>
      <span class="rule"></span>
    </div>
  </section>

</body>
</html>
```